Solar Advertising Flier to generate Biz

I need a advertisement that generates business to be used in a mailer for marketing purposes.

Im attaching a file that is a an idea of advertisement.
I do not want the "ZVN" specific information on it.
I want the background solar panels.
Same information as the ad.
And I've attached my Logo - I want the color scheme to match this.

Thank you

Target Market(s)

Middle to Upper Class Home Owners

Industry/Entity Type

Solar Energy

Requirements
Must have
• A call to action
• A professional look
Nice to have
• A family
• Great looking solar panels
Should not have
• Cartoons

```html
<!DOCTYPE html>
<html lang="en">
<head>
<meta charset="utf-8">
<title>Go Solar Flyer</title>
<link href="https://fonts.googleapis.com/css2?family=Montserrat:wght@400;500;600;700;800;900&display=swap" rel="stylesheet">
<style>
  :root {
    --blue: #1a8fd6;
    --blue-deep: #1470c4;
    --blue-light: #23aee0;
    --green: #8cc63f;
    --green-deep: #6db33f;
    --ink: #2b2b2b;
    --white: #ffffff;
    --backdrop: #d9d9d9;
  }
  * { margin: 0; padding: 0; box-sizing: border-box; }
  html, body { width: 1200px; height: 1200px; overflow: hidden; }
  body {
    background: var(--backdrop);
    font-family: "Montserrat", sans-serif;
    display: flex; align-items: center; justify-content: center;
  }
  .flyer {
    position: relative; width: 820px; height: 1160px;
    background: var(--white); overflow: hidden;
    box-shadow: 0 6px 24px rgba(0,0,0,.18);
  }
  .flyer-shapes { position: absolute; inset: 0; width: 100%; height: 100%; }
  .headline {
    position: absolute; left: 450px; top: 70px; width: 340px;
    color: var(--white); text-align: center; text-transform: uppercase;
  }
  .headline h1 { font-size: 56px; font-weight: 800; letter-spacing: 1px; line-height: 1; white-space: nowrap; }
  .headline p { font-size: 23px; font-weight: 700; line-height: 1.12; margin: 12px auto 0; width: 290px; }
  .tab {
    position: absolute; background: var(--blue-light); color: var(--white);
    font-weight: 800; text-transform: uppercase; font-size: 21px;
    padding: 10px 26px; border-radius: 0 14px 0 14px;
  }
  .tab-easy { left: 470px; top: 360px; background: var(--blue); }
  .tab-works { left: 36px; top: 586px; }
  .benefits {
    position: absolute; left: 482px; top: 420px; width: 310px;
    list-style: none; color: var(--white); font-size: 15px; font-weight: 500; line-height: 1.35;
  }
  .benefits li { padding-left: 16px; position: relative; margin-bottom: 4px; }
  .benefits li::before { content: "•"; position: absolute; left: 0; color: var(--blue-deep); }
  .benefits strong { color: var(--blue-deep); font-weight: 800; }
  .how-text {
    position: absolute; left: 60px; top: 650px; width: 360px;
    font-size: 16px; line-height: 1.55; color: var(--ink);
  }
  .how-text .hl { color: var(--blue-light); font-weight: 700; }
  .rebate {
    position: absolute; left: 388px; top: 810px; width: 160px; text-align: center;
    text-transform: uppercase; font-weight: 800; color: var(--ink); font-size: 15px; line-height: 1.15;
  }
  .rebate .amount { display: block; color: var(--green); font-size: 50px; font-weight: 900; line-height: 1; }
  .brand {
    position: absolute; left: 96px; top: 930px; display: flex; align-items: center; gap: 12px;
  }
  .brand-dot { width: 44px; height: 44px; border-radius: 50%; background: var(--green); }
  .brand-name { font-size: 22px; font-weight: 700; color: var(--blue); text-transform: uppercase; line-height: 1.05; }
  .contact {
    position: absolute; right: 40px; bottom: 34px; width: 380px;
    color: var(--white); text-align: right;
  }
  .contact .cta { font-size: 15px; font-weight: 500; }
  .contact .phone { font-size: 32px; font-weight: 800; margin: 4px 0 6px; display: flex; align-items: center; justify-content: flex-end; gap: 10px; }
  .contact .addr, .contact .web { font-size: 14px; font-weight: 500; }
  .contact .sep { color: var(--green); }
</style>
</head>
<body>
<div class="flyer">
  <svg class="flyer-shapes" viewBox="0 0 820 1160">
    <defs>
      <linearGradient id="skyPanels" x1="0" y1="0" x2="1" y2="1">
        <stop offset="0" stop-color="#9cc8ec"/>
        <stop offset=".45" stop-color="#3f63b8"/>
        <stop offset="1" stop-color="#1f2f86"/>
      </linearGradient>
      <linearGradient id="roofSky" x1="0" y1="0" x2="1" y2="1">
        <stop offset="0" stop-color="#2f86e0"/>
        <stop offset=".5" stop-color="#3a4f95"/>
        <stop offset=".8" stop-color="#b0532e"/>
        <stop offset="1" stop-color="#5d8a2e"/>
      </linearGradient>
      <linearGradient id="blueBand" x1="0" y1="0" x2="1" y2="1">
        <stop offset="0" stop-color="#1479cc"/>
        <stop offset="1" stop-color="#22a4df"/>
      </linearGradient>
      <linearGradient id="greenBand" x1="0" y1="0" x2="1" y2="1">
        <stop offset="0" stop-color="#a6d14a"/>
        <stop offset="1" stop-color="#6db33f"/>
      </linearGradient>
    </defs>
    <path class="top-band" d="M0,0 H820 V280 C640,280 470,340 360,520 L0,520 Z" fill="url(#blueBand)"/>
    <path class="green-band" d="M360,520 C470,350 640,300 820,290 V640 C700,660 640,720 610,790 C560,680 460,600 360,520 Z" fill="url(#greenBand)"/>
    <circle cx="190" cy="300" r="262" fill="var(--green)"/>
    <circle cx="190" cy="300" r="250" fill="url(#skyPanels)" role="img" aria-label="Photo of an installer fitting solar panels on a roof"/>
    <circle cx="820" cy="820" r="242" fill="var(--green)"/>
    <circle cx="820" cy="820" r="230" fill="url(#roofSky)" role="img" aria-label="Photo of solar panels on a red tile roof under a blue sky"/>
    <path class="bottom-ring" d="M240,1160 C300,1040 500,970 820,945 V960 C510,985 320,1050 262,1160 Z" fill="var(--green)"/>
    <path class="bottom-band" d="M262,1160 C320,1050 510,985 820,960 V1160 Z" fill="url(#blueBand)"/>
  </svg>

  <div class="headline">
    <h1>Go Solar</h1>
    <p>Get grandfathered before the new deadline</p>
  </div>

  <div class="tab tab-easy">We make it easy</div>
  <ul class="benefits">
    <li><strong>$0</strong> Down, no upfront cost.</li>
    <li>Save <strong>95%</strong> off your utility bill.</li>
    <li>Protect yourself from rising energy costs.</li>
    <li>Provide clean, reliable energy for your family <strong>powered by the sun.</strong></li>
  </ul>

  <div class="tab tab-works">How it works...</div>
  <p class="how-text">Your solar system allows you to <span class="hl">generate your own clean power</span> and COSTSLESS than your current utility company. Simply pay by the month, like you do now... but at a lower rate and <span class="hl">START SAVING IMMEDIATELY.</span></p>

  <div class="rebate">Call today<br>and receive a<span class="amount">$500</span>cash rebate</div>

  <div class="brand">
    <span class="brand-dot"></span>
    <span class="brand-name">Bright Valley<br>Energy</span>
  </div>

  <div class="contact">
    <p class="cta">Call Today for a no obligation consultation</p>
    <p class="phone">
      <svg width="24" height="24" viewBox="0 0 24 24" aria-hidden="true"><path fill="#fff" d="M6.6 10.8a15 15 0 0 0 6.6 6.6l2.2-2.2c.3-.3.7-.4 1-.2 1.1.4 2.3.6 3.6.6.6 0 1 .4 1 1V20c0 .6-.4 1-1 1A17 17 0 0 1 3 4c0-.6.4-1 1-1h3.5c.6 0 1 .4 1 1 0 1.3.2 2.5.6 3.6.1.3 0 .7-.2 1z"/></svg>
      000-000-0000
    </p>
    <p class="addr">1450 W Canyon Ridge Rd B-220 <span class="sep">•</span> Mesa AZ 85201</p>
    <p class="web">www.yourcompanysite.com</p>
  </div>
</div>
</body>
</html>
```